mothers day ad for martial arts school

I am looking to have a nice flyer/handout to promote my martial arts school. It is for our promotion of "mom's train free" for mothers day in May. I would like an ad that would inspire a mother to learn self defense and to improve their fitness. It can have pictures but not necessarily a requirement. Pictures don't have to be of a lady in a martial arts uniform. It may be better if they are not. It also doesn't have to be standard sheet of paper size, as these are going to be handouts the size can be smaller. I would like our Crane Hollow logo on the flyer.

Target Market(s)

mothers that hadn't thought about martial arts before but would be convinced to try it

Industry/Entity Type

School

Requirements
Must have
• text, photos that would appeal to and encourage a mother to try a self defense/fitness class
Nice to have
• our logo and text and possibly pictures that would inspire a mother to join a martial arts class

```html
<!DOCTYPE html>
<html lang="en">
<head>
<meta charset="utf-8">
<title>Mothers Train Free – Crane Hollow Martial Arts</title>
<link href="https://fonts.googleapis.com/css2?family=Barlow+Condensed:ital,wght@0,400;0,500;0,700;1,400;1,700;1,800&display=swap" rel="stylesheet">
<style>
  :root {
    --red: #d21f32;
    --red-deep: #a8102a;
    --red-light: #e2364a;
    --black: #0b0b0b;
    --white: #ffffff;
    --silver: #d9d9d9;
    --silver-light: #f4f4f4;
    --page: #ececec;
    --leaf: #6f9b35;
    --leaf-light: #b9d776;
    --teal: #3fb8c4;
  }
  * { margin: 0; padding: 0; box-sizing: border-box; }
  html, body { width: 1200px; height: 1200px; overflow: hidden; }
  body {
    background: var(--page);
    font-family: "Barlow Condensed", sans-serif;
    position: relative;
  }
  .flyer {
    position: absolute;
    left: 40px; top: 205px;
    width: 1120px; height: 790px;
    background: var(--white);
    overflow: hidden;
    box-shadow: 0 2px 6px rgba(0,0,0,.18);
  }
  .flyer-shapes { position: absolute; inset: 0; }
  .headline-line {
    position: absolute;
    line-height: 0.8;
    white-space: nowrap;
    text-transform: uppercase;
  }
  .headline-mothers { right: calc(1120px - 408px); top: 52px; font-size: 82px; font-weight: 800; font-style: italic; color: var(--white); }
  .headline-train   { right: calc(1120px - 401px); top: 112px; font-size: 142px; font-weight: 400; color: var(--black); letter-spacing: -2px; }
  .headline-free    { right: calc(1120px - 376px); top: 222px; font-size: 160px; font-weight: 800; font-style: italic; color: var(--white); }
  .headline-days    { right: calc(1120px - 353px); top: 350px; font-size: 56px; font-weight: 800; font-style: italic; color: var(--black); }
  .headline-start   { right: calc(1120px - 344px); top: 400px; font-size: 45px; font-weight: 400; font-style: italic; color: var(--white); }
  .headline-date    { right: calc(1120px - 296px); top: 442px; font-size: 45px; font-weight: 400; font-style: italic; color: var(--white); }
  .headline-date sup { font-size: 24px; vertical-align: top; line-height: 1; }

  .benefits {
    position: absolute;
    left: 67px; top: 534px;
    width: 330px;
    list-style: none;
  }
  .benefits li {
    font-size: 70px;
    font-weight: 500;
    line-height: 60px;
    height: 60px;
    white-space: nowrap;
    text-transform: uppercase;
    color: var(--black);
  }
  .benefits .accent { color: var(--red); letter-spacing: 5px; }

  .brand {
    position: absolute;
    left: 538px; top: 580px;
    display: flex; align-items: center; gap: 18px;
  }
  .brand-dot {
    width: 78px; height: 78px; border-radius: 50%;
    background: var(--red);
  }
  .brand-name {
    font-size: 66px; font-weight: 700;
    color: var(--white);
    text-transform: uppercase;
    letter-spacing: 1px;
    line-height: 1;
    white-space: nowrap;
  }
  .site-url {
    position: absolute;
    left: 811px; top: 697px;
    transform: translateX(-50%);
    font-size: 31px; font-weight: 500;
    color: var(--white);
    white-space: nowrap;
  }
</style>
</head>
<body>
  <main class="flyer">
    <svg class="flyer-shapes" width="1120" height="790" viewBox="0 0 1120 790">
      <defs>
        <linearGradient id="silverFade" x1="0" y1="0" x2="1" y2="0">
          <stop offset="0" stop-color="#ffffff"/>
          <stop offset="0.5" stop-color="#cfcfcf"/>
          <stop offset="1" stop-color="#f2f2f2"/>
        </linearGradient>
        <linearGradient id="silverBand" x1="0" y1="0" x2="0" y2="1">
          <stop offset="0" stop-color="#ffffff"/>
          <stop offset="1" stop-color="#c9c9c9"/>
        </linearGradient>
        <linearGradient id="photoTone" x1="0" y1="0" x2="1" y2="1">
          <stop offset="0" stop-color="#a9cd5f"/>
          <stop offset="0.45" stop-color="#5f8e34"/>
          <stop offset="0.75" stop-color="#3aa9b8"/>
          <stop offset="1" stop-color="#2c7fa6"/>
        </linearGradient>
      </defs>

      <!-- silver divider behind the red block -->
      <rect class="divider-left" x="380" y="0" width="110" height="520" fill="url(#silverFade)"/>
      <!-- red headline block -->
      <polygon class="headline-panel" points="0,0 422,0 484,518 0,518" fill="var(--red)"/>
      <polygon class="headline-panel-shade" points="0,0 60,0 20,518 0,518" fill="var(--red-deep)" opacity=".55"/>
      <polygon class="headline-panel-sheen" points="200,0 422,0 450,250 330,518 250,518" fill="var(--red-light)" opacity=".35"/>
      <polygon class="headline-panel-base" points="0,430 484,420 484,518 0,518" fill="var(--red-deep)" opacity=".45"/>

      <!-- benefits panel sheen -->
      <polygon class="benefits-sheen" points="0,520 486,520 486,560 0,600" fill="#f1f1f1"/>
      <polygon class="benefits-sheen" points="0,760 486,720 486,790 0,790" fill="#f1f1f1"/>
      <!-- vertical silver divider between columns -->
      <rect class="divider-center" x="484" y="0" width="6" height="790" fill="#d4d4d4"/>

      <!-- photo area -->
      <polygon class="photo-area" role="img" aria-label="Photo of two women in teal t-shirts jogging together outdoors among green trees"
        points="490,0 1120,0 1120,454 490,518" fill="url(#photoTone)"/>

      <!-- silver band under the photo -->
      <polygon class="band-silver" points="490,518 1120,454 1120,518" fill="url(#silverBand)"/>

      <!-- black brand panel -->
      <polygon class="brand-panel" points="488,518 1120,518 1120,726 867,790 547,790" fill="var(--black)"/>
      <polygon class="brand-panel-corner" points="867,790 1120,726 1120,790" fill="url(#silverBand)"/>
    </svg>

    <h1 class="headline">
      <span class="headline-line headline-mothers">Mothers</span>
      <span class="headline-line headline-train">Train</span>
      <span class="headline-line headline-free">Free</span>
      <span class="headline-line headline-days">For 30 Days</span>
      <span class="headline-line headline-start">When you start</span>
      <span class="headline-line headline-date">By May 31<sup>st</sup>!</span>
    </h1>

    <ul class="benefits">
      <li>Feel Strong</li>
      <li class="accent">Look Good</li>
      <li>Get Strong</li>
      <li class="accent">Feel Safe</li>
    </ul>

    <div class="brand">
      <span class="brand-dot"></span>
      <span class="brand-name">Crane Hollow</span>
    </div>
    <p class="site-url">https://cranehollowmartialarts.com</p>
  </main>
</body>
</html>
```